International Trading Company, 'KIRO' needs a Business Card

The company name is "KIRO" and it has own logo design.
I'd like to use its logo on this business card.
I need two side Business Card.
I'll look forward to your great design.
Thank you very much in advance.

Contact Information for Business Card

Company Name : Kiro Harbour Limited
Information Example
Dorian Pallister
Mobile(use icon please) : 1 (212) 555-0143
Tel(use icon please) : 1 (212) 555-0178
Email(use icon please) : dorian27@kiroharbour-mail.com
Address(use icon please) : 482 Halden Ave, New York, NY 10160, USA

```html
<!DOCTYPE html>
<html lang="en">
<head>
<meta charset="utf-8">
<title>KIRO Business Card</title>
<link rel="stylesheet" href="https://fonts.googleapis.com/css2?family=Montserrat:wght@500;700;800&display=swap">
<style>
  :root {
    --stage: #0c0c0c;
    --paper: #f8f6f1;
    --ink: #1f1f1f;
    --slate: #565656;
    --charcoal: #333333;
    --edge: #2a2a2a;
    --white: #ffffff;
  }
  * { box-sizing: border-box; margin: 0; padding: 0; }
  html, body {
    width: 1200px; height: 1000px; overflow: hidden;
    background: var(--stage);
    font-family: "Montserrat", Arial, sans-serif;
  }
  .stage { position: relative; width: 1200px; height: 1000px; }
  .card {
    position: absolute; left: 220px;
    width: 760px; height: 434px;
    background: var(--paper);
    overflow: hidden;
    box-shadow: 0 10px 30px rgba(0,0,0,.6);
  }
  .card--front { top: 44px; }
  .card--back { top: 522px; }
  .card__shapes { position: absolute; inset: 0; width: 760px; height: 434px; }

  .brand { position: absolute; color: var(--ink); }
  .card--front .brand { left: 70px; top: 58px; }
  .brand__name {
    font-weight: 800; font-size: 96px; line-height: 1;
    letter-spacing: 2px;
  }
  .brand__full {
    font-weight: 700; font-size: 21px; margin-top: 4px; letter-spacing: .3px;
  }
  .card--back .brand__name {
    position: absolute; left: 70px; top: 238px;
    color: var(--white); font-size: 76px;
  }

  .contact { position: absolute; left: 440px; top: 228px; color: var(--ink); }
  .contact__name { font-weight: 700; font-size: 25px; line-height: 1.1; }
  .contact__role { font-weight: 500; font-size: 15px; margin-bottom: 14px; }
  .contact__list { list-style: none; }
  .contact__item {
    display: flex; align-items: flex-start; gap: 10px;
    font-weight: 500; font-size: 16px; line-height: 21px; margin-bottom: 5px;
  }
  .contact__icon { width: 16px; height: 16px; flex: none; margin-top: 2px; fill: var(--ink); }
</style>
</head>
<body>
<main class="stage">

  <section class="card card--front" aria-label="Card front">
    <svg class="card__shapes" viewBox="0 0 760 434" aria-hidden="true">
      <polygon points="0,318 520,208 540,222 0,330" fill="var(--edge)"/>
      <polygon points="0,330 540,222 720,434 0,434" fill="var(--slate)"/>
      <polygon points="420,195 760,92 760,434 720,434 540,222 432,246" fill="var(--charcoal)"/>
    </svg>
    <div class="brand">
      <div class="brand__name">KIRO</div>
      <div class="brand__full">Kiro Harbour Limited</div>
    </div>
  </section>

  <section class="card card--back" aria-label="Card back">
    <svg class="card__shapes" viewBox="0 0 760 434" aria-hidden="true">
      <polygon points="0,0 760,0 760,110 380,250 0,250" fill="var(--slate)"/>
      <polygon points="380,250 760,110 760,118 392,258" fill="var(--edge)"/>
      <polygon points="0,0 170,0 440,252 330,434 0,434" fill="var(--charcoal)"/>
    </svg>
    <div class="brand__name">KIRO</div>
    <div class="contact">
      <div class="contact__name">Dorian Pallister</div>
      <div class="contact__role">manager</div>
      <ul class="contact__list">
        <li class="contact__item">
          <svg class="contact__icon" viewBox="0 0 24 24"><path d="M6.6 10.8a15.1 15.1 0 0 0 6.6 6.6l2.2-2.2c.3-.3.7-.4 1-.2 1.1.4 2.3.6 3.6.6.6 0 1 .4 1 1V20c0 .6-.4 1-1 1A17 17 0 0 1 3 4c0-.6.4-1 1-1h3.5c.6 0 1 .4 1 1 0 1.3.2 2.5.6 3.6.1.3 0 .7-.2 1z"/></svg>
          <span>1 (212) 555-0143</span>
        </li>
        <li class="contact__item">
          <svg class="contact__icon" viewBox="0 0 24 24"><path d="M7 1h10a2 2 0 0 1 2 2v18a2 2 0 0 1-2 2H7a2 2 0 0 1-2-2V3a2 2 0 0 1 2-2zm0 3v15h10V4z"/></svg>
          <span>1 (212) 555-0178</span>
        </li>
        <li class="contact__item">
          <svg class="contact__icon" viewBox="0 0 24 24"><path d="M2 5h20v14H2zm2 2v.5l8 5 8-5V7z"/></svg>
          <span>dorian27@kiroharbour-mail.com</span>
        </li>
        <li class="contact__item">
          <svg class="contact__icon" viewBox="0 0 24 24"><path d="M12 2a7 7 0 0 1 7 7c0 5-7 13-7 13S5 14 5 9a7 7 0 0 1 7-7zm0 4.5a2.5 2.5 0 1 0 0 5 2.5 2.5 0 0 0 0-5z"/></svg>
          <span>482 Halden Ave, New York<br>NY 10160, USA</span>
        </li>
      </ul>
    </div>
  </section>

</main>
</body>
</html>
```